Postcard Design

we need an A5 size(B: Flyer design) postcard to promote Velira Fashion, we are an evening wear company based in london se17 4qd.we specialize in party dresses, prom & evening wear. we would like to have 2 or 3 dresses featured on the card.Also note that we will be exhibiting at Malmo (Sweden) Coastway Wedding Fair on 1st & 2nd of August 2015 . The card should feature 10% off all purchases at the Malmo exhibition. For the reverse side we need normal standard postcard which we can send to our customers. The stand number will be available next week.Could you please combine 2-4 images so the card looks presentable.Nordic Bridal Show1st-2nd August 2015Stand

```html
<!DOCTYPE html>
<html lang="en">
<head>
<meta charset="utf-8">
<title>Velira Fashion – Coastway Wedding Fair Postcard</title>
<link rel="stylesheet" href="https://fonts.googleapis.com/css2?family=Raleway:wght@200&family=Oswald:wght@500;600;700&family=Open+Sans:wght@600&display=swap">
<style>
  :root {
    --stage: #3b3b3b;
    --band-dark: #4b4b4b;
    --ink: #3e3e3e;
    --ink-deep: #1f1f1f;
    --rose: #f08b8b;
    --white: #ffffff;
    --panel-top: #f4f4f4;
    --panel-bottom: #dcdcdc;
    --strip: #e6e6e6;
    --frame-dark: #4a4a4a;
    --wood: #5b3526;
    --floor: #3a2118;
    --pink-gown: #dca3b0;
    --navy-gown: #2f3d6e;
    --ivory: #efe6dc;
  }
  * { margin: 0; padding: 0; box-sizing: border-box; }
  html, body { width: 939px; height: 1200px; overflow: hidden; }
  body { background: var(--stage); position: relative; font-family: "Oswald", sans-serif; }

  .postcard { position: absolute; left: 107px; width: 729px; overflow: hidden; }
  .postcard--front { top: 47px; height: 503px; background: var(--strip); }
  .postcard--back { top: 628px; height: 512px; background: var(--white); }

  .event-band {
    position: absolute; left: 0; top: 0; width: 729px; height: 111px;
    background: var(--band-dark);
    display: flex; align-items: center; justify-content: center;
    font-family: "Raleway", sans-serif; font-weight: 200;
    font-size: 50px; color: var(--white); letter-spacing: 0.5px;
    text-transform: uppercase;
  }
  .photo { position: absolute; }
  .photo--pink-gown { left: 0; top: 111px; width: 205px; height: 374px;
    background:
      radial-gradient(ellipse 22% 46% at 40% 56%, var(--pink-gown) 0%, rgba(220,163,176,0.85) 55%, rgba(220,163,176,0) 100%),
      linear-gradient(180deg, #8a5a3e 0%, var(--wood) 8%, #6a4434 60%, var(--floor) 72%, #4a2a1e 100%); }
  .photo--navy-gown { left: 525px; top: 111px; width: 204px; height: 374px;
    background:
      radial-gradient(ellipse 20% 46% at 50% 58%, var(--navy-gown) 0%, rgba(47,61,110,0.85) 55%, rgba(47,61,110,0) 100%),
      linear-gradient(180deg, #8a5a3e 0%, var(--wood) 8%, #6a4434 60%, var(--floor) 72%, #4a2a1e 100%); }

  .promo-panel {
    position: absolute; left: 205px; top: 111px; width: 320px; height: 374px;
    background: linear-gradient(180deg, var(--panel-top), var(--panel-bottom));
    text-align: center;
  }
  .brand-name { position: absolute; left: 0; right: 0; top: 32px;
    font-weight: 500; font-size: 38px; line-height: 1.2;
    color: var(--ink); letter-spacing: 3px; }
  .headline { position: absolute; left: 0; right: 0; line-height: 1; }
  .headline--exhibition { top: 98px; font-weight: 600; font-size: 60px; color: var(--ink); }
  .headline--fashion { top: 168px; font-weight: 600; font-size: 78px; color: var(--rose); }
  .web-address { position: absolute; left: 0; right: 0; top: 276px;
    font-family: "Open Sans", sans-serif; font-weight: 600; font-size: 14px;
    color: var(--ink); letter-spacing: 2px; }
  .date-band { position: absolute; left: 0; bottom: 0; width: 320px; height: 56px;
    background: var(--rose); color: var(--white);
    display: flex; align-items: center; justify-content: center;
    font-weight: 500; font-size: 25px; letter-spacing: 0.3px; }

  .photo--ivory-gown { left: 0; top: 0; width: 213px; height: 512px;
    background:
      radial-gradient(ellipse 40% 58% at 45% 62%, var(--ivory) 0%, rgba(239,230,220,0.9) 60%, rgba(239,230,220,0) 100%),
      linear-gradient(180deg, #bfae98 0%, #d8cbbb 30%, #c9bba8 65%, #b8a994 100%); }
  .frame { position: absolute; }
  .frame--logo-field { left: 213px; top: 0; width: 132px; height: 65px; background: var(--white); }
  .frame--rose-rail { left: 345px; top: 0; width: 13px; height: 405px; background: var(--rose); }
  .frame--dark-rail { left: 358px; top: 0; width: 5px; height: 418px; background: var(--frame-dark); }
  .frame--lower-field { left: 106px; top: 418px; width: 257px; height: 94px; background: var(--white); }
  .frame--dark-base { left: 88px; top: 405px; width: 275px; height: 13px; background: var(--frame-dark); }
  .frame--rose-side { left: 88px; top: 297px; width: 13px; height: 215px; background: var(--rose); }
  .frame--dark-side { left: 101px; top: 418px; width: 5px; height: 94px; background: var(--frame-dark); }
  .back-brand { position: absolute; left: 213px; top: 22px; width: 132px; text-align: center;
    font-weight: 500; font-size: 26px; line-height: 1.2; color: var(--ink); letter-spacing: 2px; }
  .photo--portrait { left: 213px; top: 65px; width: 132px; height: 222px;
    background:
      radial-gradient(ellipse 55% 40% at 60% 85%, #f3e6d8 0%, rgba(243,230,216,0) 100%),
      linear-gradient(180deg, #cfe0ec 0%, #dfe3e4 40%, #e8d6c3 70%, #efe2d4 100%); }
  .offer-box { position: absolute; left: 88px; top: 297px; width: 257px; height: 108px;
    background: var(--rose); text-align: center; }
  .offer-amount { display: block; margin-top: 6px; font-weight: 700; font-size: 62px;
    line-height: 1; color: var(--white); letter-spacing: 0.5px; }
  .offer-note { display: block; margin-top: 6px; font-weight: 600; font-size: 23px;
    line-height: 1.2; color: var(--ink-deep); }
</style>
</head>
<body>
  <section class="postcard postcard--front">
    <header class="event-band">Coastway Wedding Fair</header>
    <div class="photo photo--pink-gown" role="img" aria-label="Model in a full-length pink sequinned evening gown with a pink chiffon scarf on a wooden stage"></div>
    <div class="promo-panel">
      <div class="brand-name">Velira</div>
      <div class="headline headline--exhibition">EXHIBITION</div>
      <div class="headline headline--fashion">FASHION</div>
      <div class="web-address">www.velirafashion.com</div>
      <div class="date-band">1ST-2ND AUGUST 2015 STAND</div>
    </div>
    <div class="photo photo--navy-gown" role="img" aria-label="Model in a navy sequinned fishtail evening gown with a jewelled neckline on a wooden stage"></div>
  </section>

  <section class="postcard postcard--back">
    <div class="photo photo--ivory-gown" role="img" aria-label="Model in an ivory chiffon gown with an embellished bodice, standing outdoors"></div>
    <div class="frame frame--logo-field"></div>
    <div class="back-brand">Velira</div>
    <div class="photo photo--portrait" role="img" aria-label="Side profile portrait of a model in an ivory beaded dress against a pale sky"></div>
    <div class="frame frame--lower-field"></div>
    <div class="frame frame--dark-rail"></div>
    <div class="frame frame--rose-rail"></div>
    <div class="frame frame--dark-base"></div>
    <div class="frame frame--dark-side"></div>
    <div class="frame frame--rose-side"></div>
    <div class="offer-box">
      <span class="offer-amount">10%OFF</span>
      <span class="offer-note">MALMO EXHIBITION CARD</span>
    </div>
  </section>
</body>
</html>
```